Pin Oak Media Outdoor Advertising Corporate Stationery Design

We need a full corporate stationary design for our company Pin Oak Media. We setup and lease billboards, building wraps, trailer ads and construction hoardings.

We need to establish our branding and our newly created logo. All our brand identity should point towards our values, vision and mission.

We are open to fresh new ideas for our stationary design as long as it ultimately reflects the brand & logo.

Corporate Stationary List:
1. Business Card Design
2. Letterhead Design
3. Email Signature Design
4. “Advertise Here” Design (for placement on empty billboards, etc)

All designs must include our logo and be kept simple, modern, friendly and effective.

All designs should please be provided in Illustrator, Photoshop and InDesign file formats.

More details are attached in Word.

Hey

The project has been guaranteed. We like what has been submitted so far but we''d like to see a few concepts for the "Advertise Here" design for open billboards please.

Thanks!

Target Market(s)

Male and female, corporates, business owners, media buying agencies, government & all age groups.

Industry/Entity Type

Construction

Requirements
Must have
• All designs must incorporate our colours: Pantone 319C, 320C, 321C & Hexachrome Black C.

1.Business Card Design
a. Logo
b. Name
c. Mobile
d. Landline
e. Website
f. Facebook
g. Twitter
2. Letterhead Design
a. Logo
b. Mobile
c. Landline
d. Website
e. CC reg number
f. BEE level 4 contributor
g. PRTVA member
h. Postal Address
3. Email Signature Design
a. Logo
b. Name
c. Mobile
d. Landline
e. BEE level 4 contributor
f. PRTVA member
g. Website
h. Facebook
i. Twitter
4. “Advertise Here” Design (for placement on empty billboards, etc) Majority ratio of 2:1 (eg 6m wide by 3m high) - Please use 2 attached photos.
a. Logo .co.za
b. Contact Mirela
c. Mobile
Nice to have
• Come up with a cool slogan / tagline for Business Cards, “Advertise Here” Design

```html
<!DOCTYPE html>
<html lang="en">
<head>
<meta charset="utf-8">
<title>Pin Oak Media – Business Card</title>
<link rel="stylesheet" href="https://fonts.googleapis.com/css2?family=Open+Sans:wght@400;600;700&family=Arimo:wght@400&display=swap">
<style>
  :root {
    --stage: #5b5b5b;
    --card-dark: #000000;
    --card-light: #ffffff;
    --teal-deep: #0aa2b3;
    --teal-light: #6dcdd3;
    --ink: #111111;
    --white: #ffffff;
  }
  html, body {
    margin: 0;
    width: 1200px;
    height: 534px;
    overflow: hidden;
    background: var(--stage);
  }
  .stage {
    position: relative;
    width: 1200px;
    height: 534px;
  }
  .card {
    position: absolute;
    top: 117px;
    width: 525px;
    height: 300px;
    border-radius: 22px;
    overflow: hidden;
  }
  .card--front { left: 62px; background: var(--card-dark); }
  .card--back { left: 621px; background: var(--card-light); }
  .card__band {
    position: absolute;
    left: 0;
    bottom: 0;
    width: 525px;
    height: 18px;
    display: block;
  }
  .front__wordmark {
    position: absolute;
    left: 46px;
    top: 178px;
    margin: 0;
    font-family: "Open Sans", sans-serif;
    font-weight: 600;
    font-size: 50px;
    line-height: 1;
    color: var(--white);
    letter-spacing: -0.5px;
  }
  .front__web {
    position: absolute;
    left: 200px;
    top: 235px;
    font-family: "Arimo", sans-serif;
    font-size: 12.5px;
    letter-spacing: 2px;
    color: var(--white);
  }
  .back__wordmark {
    position: absolute;
    left: 37px;
    top: 98px;
    margin: 0;
    font-family: "Open Sans", sans-serif;
    font-weight: 600;
    font-size: 25px;
    line-height: 1;
    color: var(--teal-deep);
  }
  .back__person {
    position: absolute;
    right: 38px;
    top: 96px;
    text-align: right;
    font-family: "Arimo", sans-serif;
  }
  .back__name {
    margin: 0;
    font-size: 20px;
    line-height: 1;
    color: var(--ink);
  }
  .back__role {
    margin: 2px 0 0;
    font-size: 12px;
    line-height: 1;
    color: var(--teal-light);
  }
  .contact {
    position: absolute;
    left: 31px;
    top: 170px;
    margin: 0;
    padding: 0;
    list-style: none;
    font-family: "Arimo", sans-serif;
    color: var(--ink);
  }
  .contact__item {
    display: flex;
    align-items: center;
    gap: 6px;
    font-size: 13.5px;
    line-height: 1;
    margin-bottom: 7px;
  }
  .contact__item--phone { font-size: 17px; margin-top: 2px; }
  .contact__icon { width: 12px; height: 12px; flex: none; fill: var(--teal-light); }
</style>
</head>
<body>
<main class="stage">

  <section class="card card--front" aria-label="Business card front">
    <h1 class="front__wordmark">Pin Oak Media</h1>
    <span class="front__web">www.pinoakmedia.com</span>
    <svg class="card__band" viewBox="0 0 525 18" aria-hidden="true">
      <rect width="525" height="18" fill="var(--teal-deep)"/>
      <polygon points="370,0 525,0 525,18 357,18" fill="var(--teal-light)"/>
    </svg>
  </section>

  <section class="card card--back" aria-label="Business card back">
    <h2 class="back__wordmark">Pin Oak Media</h2>
    <div class="back__person">
      <p class="back__name">Dara Whitfield</p>
      <p class="back__role">Manager</p>
    </div>
    <ul class="contact">
      <li class="contact__item">
        <svg class="contact__icon" viewBox="0 0 12 12" aria-hidden="true"><polygon points="6,1 11,6 9.5,6 9.5,11 7,11 7,8 5,8 5,11 2.5,11 2.5,6 1,6"/></svg>
        2408 Larkspur Lane, Millbrook, FL 32011
      </li>
      <li class="contact__item contact__item--phone">
        <svg class="contact__icon" viewBox="0 0 12 12" aria-hidden="true"><rect x="3" y="0" width="6" height="12" rx="1"/><rect x="4" y="2" width="4" height="4" fill="#fff"/></svg>
        400 555 0199
      </li>
      <li class="contact__item">
        <svg class="contact__icon" viewBox="0 0 12 12" aria-hidden="true"><path d="M1 5 L6 2 L11 5 L11 11 L1 11 Z"/><path d="M1.5 5.5 L6 8.5 L10.5 5.5" stroke="#fff" stroke-width="0.8" fill="none"/></svg>
        hello@pinoakmedia.com
      </li>
      <li class="contact__item">
        <svg class="contact__icon" viewBox="0 0 12 12" aria-hidden="true"><circle cx="6" cy="6" r="5.5"/><g stroke="#fff" stroke-width="0.7" fill="none"><ellipse cx="6" cy="6" rx="2.3" ry="5.3"/><line x1="0.5" y1="6" x2="11.5" y2="6"/></g></svg>
        www.pinoakmedia.com
      </li>
    </ul>
    <svg class="card__band" viewBox="0 0 525 18" aria-hidden="true">
      <rect width="525" height="18" fill="var(--teal-deep)"/>
      <polygon points="370,0 525,0 525,18 357,18" fill="var(--teal-light)"/>
    </svg>
  </section>

</main>
</body>
</html>
```